Bim Tash Brochure Design

We are a Marketing company offering different services. Services must be outlined on design we will provive text for the services once project is accepted.

Service Titles to include in design

Corporate Branding
Marketing
Web Design 
Business Consultation
Printing
Mailing
Automation
Bim Tash Pick

Please post designs, we have n

Target Market(s)

18+ Years Old

Must have
• Web 2.0 Graphics
• Eye catching design
Nice to have
• Rich Graphics
• Creativity
Should not have
• Standard Templates
• Only bullets

```html
<!DOCTYPE html>
<html lang="en">
<head>
<meta charset="utf-8">
<title>Bim Tash Brochure</title>
<link href="https://fonts.googleapis.com/css2?family=Arimo:wght@400;700&display=swap" rel="stylesheet">
<style>
  :root {
    --orange: #f7931e;
    --orange-deep: #f26a10;
    --orange-light: #fbb040;
    --yellow: #fff200;
    --red-orange: #e8400c;
    --ink: #111111;
    --grey: #8a8a8a;
    --white: #ffffff;
    --panel: rgba(255, 214, 160, 0.55);
  }
  * { box-sizing: border-box; margin: 0; padding: 0; }
  html, body { width: 800px; height: 1200px; overflow: hidden; }
  body {
    background: var(--white);
    font-family: "Arimo", Arial, sans-serif;
    position: relative;
  }
  .spread {
    position: absolute;
    left: 20px;
    width: 760px;
    height: 540px;
    box-shadow: 4px 5px 6px rgba(0,0,0,0.45);
    overflow: hidden;
  }
  .spread--outside { top: 30px; display: flex; }
  .spread--inside {
    top: 615px;
    background: radial-gradient(ellipse at 35% 40%, var(--orange-light) 0%, var(--orange) 50%, var(--orange-deep) 100%);
  }

  /* Outside: three panels */
  .panel { position: relative; width: 253.33px; height: 100%; }
  .panel + .panel { border-left: 1px solid rgba(255,255,255,0.35); }
  .panel--intro { background: linear-gradient(160deg, var(--orange-light), var(--orange) 55%, var(--orange-deep)); }
  .panel--contact, .panel--cover { background: linear-gradient(180deg, var(--orange) 0%, var(--orange-deep) 78%); }

  .body-copy {
    color: var(--yellow);
    font-size: 10.5px;
    line-height: 1.32;
  }
  .body-copy p + p { margin-top: 12px; }
  .panel--intro .body-copy { position: absolute; left: 20px; top: 40px; width: 215px; }
  .intro-art {
    position: absolute; left: 0; bottom: 0; width: 100%; height: 250px;
    background: radial-gradient(ellipse at 40% 55%, rgba(232,64,12,0.35), rgba(247,147,30,0) 70%);
  }

  .pull-quote {
    color: var(--yellow);
    font-size: 19px;
    line-height: 1.15;
    position: relative;
  }
  .pull-quote .mark { font-family: Georgia, serif; font-size: 26px; font-weight: 700; line-height: 0; }
  .panel--contact .pull-quote { position: absolute; left: 20px; top: 28px; width: 220px; }

  .contact { position: absolute; left: 20px; top: 162px; width: 220px; }
  .contact-title {
    display: flex; align-items: center; gap: 8px;
    color: var(--yellow); font-size: 12px; margin-bottom: 8px;
  }
  .contact-lines { color: var(--white); font-size: 8.5px; line-height: 1.38; font-weight: 700; padding-left: 28px; }
  .contact-lines p + p { margin-top: 0; }
  .map-art {
    position: absolute; left: 15px; top: 290px; width: 225px; height: 110px;
    background: radial-gradient(ellipse at 50% 50%, rgba(255,242,0,0.55), rgba(247,147,30,0) 72%);
  }

  .cover-art {
    position: absolute; left: 0; top: 0; width: 100%; height: 450px;
    background: radial-gradient(ellipse at 72% 45%, var(--yellow) 0%, var(--orange-light) 30%, var(--orange) 60%, var(--red-orange) 100%);
  }

  .white-strip {
    position: absolute; left: 0; bottom: 0; width: 100%; height: 90px;
    background: var(--white);
    display: flex; align-items: center;
  }
  .panel--contact .white-strip { padding-left: 16px; }
  .panel--cover .white-strip { justify-content: flex-end; padding-right: 18px; }
  .brand {
    display: flex; align-items: center; gap: 6px;
    color: var(--orange); font-weight: 700; font-size: 20px;
  }
  .brand-dot { width: 14px; height: 14px; border-radius: 50%; background: var(--orange); }

  .arrow-icon { width: 20px; height: 20px; flex: none; }

  /* Inside */
  .inside-intro { position: absolute; left: 20px; top: 22px; width: 215px; }
  .inside-intro .pull-quote { font-size: 19.5px; margin-bottom: 18px; }
  .people-art {
    position: absolute; left: 12px; bottom: 0; width: 220px; height: 160px;
    background: linear-gradient(180deg, #d9d9d9, #a8a8a8);
    border-radius: 60px 60px 0 0;
    opacity: 0.85;
  }

  .services {
    position: absolute; left: 255px; top: 20px; width: 485px; height: 500px;
    background: var(--panel);
    border-radius: 18px;
    display: grid;
    grid-template-columns: 1fr 1fr;
    grid-template-rows: repeat(4, 1fr);
    column-gap: 24px;
    padding: 16px 18px 8px 14px;
  }
  .service-title {
    display: flex; align-items: center; gap: 8px;
    color: var(--red-orange); font-size: 12px; margin-bottom: 6px;
  }
  .service-text {
    color: var(--ink); font-size: 8.6px; line-height: 1.36;
    padding-left: 28px;
  }
</style>
</head>
<body>

<section class="spread spread--outside">
  <div class="panel panel--intro">
    <div class="body-copy">
      <p>Lorem ipsum dolor sit amet, consectetuer adipiscing elit. Quisque sit amet arcu. Nunc eu turpis. Nulla facilisi. Curabitur vulputate imperdiet mauris. Quisque vitae elit bibendum dolor mattis feugiat. Duis molestie. Aenean ornare mauris et sapien. Nullam et arcu id libero interdum accumsan. Mauris diam lacus, vehicula sollicitudin, tempus vitae, ultricies nec, metus. Aliquam erat volutpat. Donec ac quam sit amet ligula faucibus lacinia. Morbi vel nisi. Ut nibh. Nullam vehicula viverra lacus.</p>
      <p>Nulla pretium eros ut felis. Cum sociis natoque penatibus et magnis dis parrient montes, nascetur ridiculus mus. Suspendisse placerat nulla eu metus.</p>
    </div>
    <div class="intro-art" role="img" aria-label="Handwritten script and soft oval shapes in deep orange"></div>
  </div>

  <div class="panel panel--contact">
    <p class="pull-quote"><span class="mark">&ldquo;</span><br>Nulla pretium eros ut felis. Cum sois natoue penatibus et magnis dis parturient monte. <span class="mark">&rdquo;</span></p>
    <div class="contact">
      <div class="contact-title">
        <svg class="arrow-icon" viewBox="0 0 20 20" aria-hidden="true"><circle cx="10" cy="10" r="10" fill="#1a1a1a"/><path d="M8 5.5 L12.5 10 L8 14.5" fill="none" stroke="#35b6e8" stroke-width="2.2" stroke-linecap="round" stroke-linejoin="round"/></svg>
        Contact Us
      </div>
      <div class="contact-lines">
        <p>Cras et mauris nec arcu scelerisque rutrum.</p>
        <p>Vivamus ut ipsum. Integer enim</p>
        <p>T. 00 0000 0000</p>
        <p>F. 00 0000 0000</p>
        <p>E. info@bimtash.com</p>
        <p>www.bimtash.com</p>
      </div>
    </div>
    <div class="map-art" role="img" aria-label="Striped yellow world map"></div>
    <div class="white-strip">
      <div class="brand"><span class="brand-dot"></span>Bim Tash</div>
    </div>
  </div>

  <div class="panel panel--cover">
    <div class="cover-art" role="img" aria-label="Grid of glowing orange, red and yellow dots"></div>
    <div class="white-strip">
      <div class="brand"><span class="brand-dot"></span>Bim Tash</div>
    </div>
  </div>
</section>

<section class="spread spread--inside">
  <div class="inside-intro">
    <p class="pull-quote"><span class="mark">&ldquo;</span><br>Lorem ipsum dolor sit amet, consectetuer adipiscing elit. <span class="mark">&rdquo;</span></p>
    <div class="body-copy">
      <p>Lorem ipsum dolor sit amet, consectetuer adipiscing elit. Quisque sit amet arcu. Nunc eu turpis. Nulla facilisi. Curabitur vulputate imperdiet mauris. Quisque vitae elit bibendum dolor mattis feugiat. Duis molestie. Aenean ornare mauris et sapien. Nullam et arcu id libero interdum accumsan. Mauris diam lacus, vehicula sollicitudin, tempus vitae, ultricies nec, metus. Aliquam erat volutpat. Donec ac quam sit amet ligula faucibus lacinia. Morbi vel nisi. Ut nibh. Nullam vehicula viverra lacus.</p>
      <p>Nulla pretium eros ut felis. Cum sociis natoque penatibus et magnis dis parrient montes, nascetur ridiculus mus. Suspendisse placerat nulla eu metus.</p>
    </div>
  </div>
  <div class="people-art" role="img" aria-label="Silver silhouettes of a group of young people"></div>

  <div class="services">
    <article class="service">
      <h3 class="service-title"><svg class="arrow-icon" viewBox="0 0 20 20" aria-hidden="true"><circle cx="10" cy="10" r="10" fill="#1a1a1a"/><path d="M8 5.5 L12.5 10 L8 14.5" fill="none" stroke="#35b6e8" stroke-width="2.2" stroke-linecap="round" stroke-linejoin="round"/></svg><span style="font-weight:400">Corporate Branding</span></h3>
      <p class="service-text">Cras et mauris nec arcu scelerisque rutrum. Vivamus ut ipsum. Integer enim ipsum, venenatis a, eleifend et, egestas vitae, lorem. Pellentesque molestie, dolor sed commodo congue, felis est gravida tortor, nec ultricies lorem lorem ut justo. Integer neque ligula, ultricies a, tempus a, fermentum e.</p>
    </article>
    <article class="service">
      <h3 class="service-title"><svg class="arrow-icon" viewBox="0 0 20 20" aria-hidden="true"><circle cx="10" cy="10" r="10" fill="#1a1a1a"/><path d="M8 5.5 L12.5 10 L8 14.5" fill="none" stroke="#35b6e8" stroke-width="2.2" stroke-linecap="round" stroke-linejoin="round"/></svg><span style="font-weight:400">Printing</span></h3>
      <p class="service-text">Cras et mauris nec arcu scelerisque rutrum. Vivamus ut ipsum. Integer enim ipsum, venenatis a, eleifend et, egestas vitae, lorem. Pellentesque molestie, dolor sed commodo congue, felis est gravida tortor, nec ultricies lorem lorem ut justo. Integer neque ligula, ultricies a, tempus a, fermentum e.</p>
    </article>
    <article class="service">
      <h3 class="service-title"><svg class="arrow-icon" viewBox="0 0 20 20" aria-hidden="true"><circle cx="10" cy="10" r="10" fill="#1a1a1a"/><path d="M8 5.5 L12.5 10 L8 14.5" fill="none" stroke="#35b6e8" stroke-width="2.2" stroke-linecap="round" stroke-linejoin="round"/></svg><span style="font-weight:400">Marketing</span></h3>
      <p class="service-text">Cras et mauris nec arcu scelerisque rutrum. Vivamus ut ipsum. Integer enim ipsum, venenatis a, eleifend et, egestas vitae, lorem. Pellentesque molestie, dolor sed commodo congue, felis est gravida tortor, nec ultricies lorem lorem ut justo. Integer neque ligula, ultricies a, tempus a, fermentum e.</p>
    </article>
    <article class="service">
      <h3 class="service-title"><svg class="arrow-icon" viewBox="0 0 20 20" aria-hidden="true"><circle cx="10" cy="10" r="10" fill="#1a1a1a"/><path d="M8 5.5 L12.5 10 L8 14.5" fill="none" stroke="#35b6e8" stroke-width="2.2" stroke-linecap="round" stroke-linejoin="round"/></svg><span style="font-weight:400">Mailing</span></h3>
      <p class="service-text">Cras et mauris nec arcu scelerisque rutrum. Vivamus ut ipsum. Integer enim ipsum, venenatis a, eleifend et, egestas vitae, lorem. Pellentesque molestie, dolor sed commodo congue, felis est gravida tortor, nec ultricies lorem lorem ut justo. Integer neque ligula, ultricies a, tempus a, fermentum e.</p>
    </article>
    <article class="service">
      <h3 class="service-title"><svg class="arrow-icon" viewBox="0 0 20 20" aria-hidden="true"><circle cx="10" cy="10" r="10" fill="#1a1a1a"/><path d="M8 5.5 L12.5 10 L8 14.5" fill="none" stroke="#35b6e8" stroke-width="2.2" stroke-linecap="round" stroke-linejoin="round"/></svg><span style="font-weight:400">Web Design</span></h3>
      <p class="service-text">Cras et mauris nec arcu scelerisque rutrum. Vivamus ut ipsum. Integer enim ipsum, venenatis a, eleifend et, egestas vitae, lorem. Pellentesque molestie, dolor sed commodo congue, felis est gravida tortor, nec ultricies lorem lorem ut justo. Integer neque ligula, ultricies a, tempus a, fermentum e.</p>
    </article>
    <article class="service">
      <h3 class="service-title"><svg class="arrow-icon" viewBox="0 0 20 20" aria-hidden="true"><circle cx="10" cy="10" r="10" fill="#1a1a1a"/><path d="M8 5.5 L12.5 10 L8 14.5" fill="none" stroke="#35b6e8" stroke-width="2.2" stroke-linecap="round" stroke-linejoin="round"/></svg><span style="font-weight:400">Automation</span></h3>
      <p class="service-text">Cras et mauris nec arcu scelerisque rutrum. Vivamus ut ipsum. Integer enim ipsum, venenatis a, eleifend et, egestas vitae, lorem. Pellentesque molestie, dolor sed commodo congue, felis est gravida tortor, nec ultricies lorem lorem ut justo. Integer neque ligula, ultricies a, tempus a, fermentum e.</p>
    </article>
    <article class="service">
      <h3 class="service-title"><svg class="arrow-icon" viewBox="0 0 20 20" aria-hidden="true"><circle cx="10" cy="10" r="10" fill="#1a1a1a"/><path d="M8 5.5 L12.5 10 L8 14.5" fill="none" stroke="#35b6e8" stroke-width="2.2" stroke-linecap="round" stroke-linejoin="round"/></svg><span style="font-weight:400">Business Consultation</span></h3>
      <p class="service-text">Cras et mauris nec arcu scelerisque rutrum. Vivamus ut ipsum. Integer enim ipsum, venenatis a, eleifend et, egestas vitae, lorem. Pellentesque molestie, dolor sed commodo congue, felis est gravida tortor, nec ultricies lorem lorem ut justo. Integer neque ligula, ultricies a, tempus a, fermentum e.</p>
    </article>
    <article class="service">
      <h3 class="service-title"><svg class="arrow-icon" viewBox="0 0 20 20" aria-hidden="true"><circle cx="10" cy="10" r="10" fill="#1a1a1a"/><path d="M8 5.5 L12.5 10 L8 14.5" fill="none" stroke="#35b6e8" stroke-width="2.2" stroke-linecap="round" stroke-linejoin="round"/></svg><span style="font-weight:400">Bim Tash Pick</span></h3>
      <p class="service-text">Cras et mauris nec arcu scelerisque rutrum. Vivamus ut ipsum. Integer enim ipsum, venenatis a, eleifend et, egestas vitae, lorem. Pellentesque molestie, dolor sed commodo congue, felis est gravida tortor, nec ultricies lorem lorem ut justo. Integer neque ligula, ultricies a, tempus a, fermentum e.</p>
    </article>
  </div>
</section>

</body>
</html>
```